Bar Crawl Website required

Hi,

I need a new website (www.gladtonightwalk.com) to have the company information on one page (2 maximum) with an auto responder.
I will need to be shown how to update the site and use of auto responder. And I’m looking to build the site further as the crawls grow.
Ideally to be worked on with SEO – looking on Google for these words:

Best bars in London
Pub crawl London
Night out London
Bars London

I want the writing to be clear, concise and easily read in UK English but I need the design to be fun and cool (as its promoting a bar crawl).
We’re looking to drive people to the site and then attend a night. We’re targeting 18-35 year olds who live in London and want to party.
I want the picture gallery to look cool, the benefits clear to see and easy for the customer to sign up (website takes e-mail address)
We run bar crawls and our service is free to the customer, which we want to be prevalent but I want it to look like a trustworthy site and not one that is just trying to "sell" ie "whats the catch"?. Really want the website to be fun too and not over a background image.
I have provided the content (attached) but looking for you to come up with a design that is engaging, fun but also clear to read.

Examples:
http://www.morvalinnhop.com/
http://www.7loudeveningtrip.com/index.php?option=com_content&view=article&id=1&Itemid=1
http://www.hullabalootrek.com/

Thanks,
Updates

Hi,

The name of the company is called "Glad Tonight Walk".
Please can the benefits (free entry, free shot etc)  as per my word document be included on the homepage.
Can the content/structure be more similar to my word document that I uploaded.

Thanks,

Kit

Target Market(s)

18-35 year olds in London who like a night out.

Industry/Entity Type

It Company

Requirements
Must have
• Cool Photo Gallery
Autoresponder
Calendar with dates of crawls (I need to be able to update this)
Ideally on one page but will look at 2 pages if 1 page is not enough.
Should not have
• No Cheap looking background

```html
<!DOCTYPE html>
<html lang="en-GB">
<head>
<meta charset="utf-8">
<title>Glad Tonight Walk – London's Biggest and Best Night Out</title>
<link rel="stylesheet" href="https://fonts.googleapis.com/css2?family=Oswald:wght@500&family=Arimo:wght@400;700&family=Francois+One&display=swap">
<style>
  :root {
    --paper: #efebe5;
    --ink: #1c1c1c;
    --body: #3a3632;
    --orange: #e8600f;
    --orange-light: #f7a21b;
    --ribbon: #f2a81d;
    --teal: #13968f;
    --teal-dark: #0d7c76;
    --green: #3d8a1e;
    --panel: #ecebea;
    --panel-inner: #dfdcd8;
    --tan: #c9bba6;
    --tan-dark: #b4a48c;
    --white: #ffffff;
    --muted: #6b665f;
    --social-dark: #2b4a8a;
    --social-light: #3aa6d8;
  }
  * { box-sizing: border-box; margin: 0; padding: 0; }
  html, body { width: 1000px; height: 1200px; overflow: hidden; }
  body {
    position: relative;
    background: var(--paper);
    font-family: "Arimo", Arial, sans-serif;
    color: var(--ink);
  }
  .abs { position: absolute; }

  /* Header */
  .brand {
    left: 160px; top: 40px; width: 220px; height: 90px;
    display: flex; align-items: center; gap: 10px;
  }
  .brand-dot { width: 34px; height: 34px; border-radius: 50%; background: var(--orange); flex: none; }
  .brand-name {
    font-family: "Francois One", sans-serif; font-size: 30px; line-height: 32px;
    color: var(--orange); text-transform: uppercase;
  }
  .party-art {
    left: 412px; top: 6px; width: 240px; height: 158px;
    background: linear-gradient(90deg, #e9e0d3 0%, #f0d8c8 60%, #eed3cf 100%);
    border-radius: 6px;
  }
  .party-art.side {
    left: 712px; top: 52px; width: 90px; height: 112px;
    background: linear-gradient(#f3e3c3, #efe0cc);
  }
  .auth-btn {
    top: 13px; height: 29px; width: 78px;
    font-family: "Francois One", sans-serif; font-size: 17px; color: var(--white);
    display: flex; align-items: center; justify-content: center; gap: 6px;
    border-radius: 3px; box-shadow: 0 2px 3px rgba(0,0,0,.25); text-decoration: none;
  }
  .auth-btn.login { left: 670px; background: linear-gradient(#5aa82d, var(--green)); }
  .auth-btn.signup { left: 762px; background: linear-gradient(#f9b531, #ea8c10); }
  .banner {
    left: 152px; top: 165px; width: 696px; height: 33px;
    background: linear-gradient(var(--orange-light), var(--ribbon) 60%, #e48d12);
    border-radius: 3px 3px 10px 10px;
    font-family: "Oswald", sans-serif; font-size: 21px; letter-spacing: .4px;
    color: var(--white); text-align: center; line-height: 33px; text-transform: uppercase;
  }

  .section-title {
    font-family: "Francois One", sans-serif; font-size: 19px; color: var(--orange);
    text-transform: uppercase; font-weight: 400;
  }

  /* Gallery */
  .gallery-frame {
    left: 155px; top: 238px; width: 290px; height: 174px;
    background: var(--white); box-shadow: 0 2px 6px rgba(0,0,0,.2);
  }
  .gallery-photo {
    left: 160px; top: 246px; width: 278px; height: 160px;
    background: linear-gradient(120deg, #2d3c8e 0%, #b2324a 45%, #d83a32 70%, #3a2a60 100%);
  }
  .thumbs { left: 153px; top: 430px; width: 296px; height: 27px; }
  .thumb {
    position: absolute; top: 0; width: 27px; height: 27px; border: 2px solid var(--white);
    box-shadow: 0 1px 2px rgba(0,0,0,.3);
  }

  /* Benefits */
  .benefits-title {
    left: 505px; top: 210px; font-family: "Arimo", Arial, sans-serif; font-weight: 700; font-size: 18px;
    color: var(--ink); text-transform: uppercase;
  }
  .benefits-title em { font-style: normal; color: var(--orange); }
  .dashed { border-top: 1px dashed #b6b0a7; height: 0; }
  .benefit { left: 508px; width: 340px; font-size: 15px; line-height: 19px; display: flex; gap: 8px; }
  .benefit svg { flex: none; margin-top: 3px; }
  .benefit strong { color: var(--orange); font-weight: 700; }

  /* Signup */
  .signup-card {
    left: 155px; top: 480px; width: 290px; height: 161px; background: var(--white);
    box-shadow: 0 2px 6px rgba(0,0,0,.2);
  }
  .signup-copy {
    left: 160px; top: 486px; width: 280px; text-align: center;
    font-size: 10.5px; line-height: 17px; color: var(--body); text-transform: uppercase;
  }
  .signup-band {
    left: 165px; top: 563px; width: 270px; height: 68px;
    background: linear-gradient(var(--teal), var(--teal-dark));
  }
  .email-field {
    left: 178px; top: 580px; width: 246px; height: 36px; display: flex;
    border-radius: 4px; overflow: hidden; box-shadow: 0 0 0 2px rgba(255,255,255,.5);
  }
  .email-field span {
    flex: 1; background: var(--white); font-size: 11px; color: #9a958f;
    line-height: 36px; padding-left: 8px;
  }
  .email-field b {
    width: 86px; background: linear-gradient(#f5821f, #e55a0d);
    font-family: "Francois One", sans-serif; font-weight: 400; font-size: 22px;
    color: var(--white); text-align: center; line-height: 36px;
  }

  /* Events */
  .event-date { width: 34px; height: 52px; }
  .event-title { font-size: 10.5px; font-weight: 400; color: var(--ink); }
  .event-text { font-size: 8.5px; line-height: 13px; color: var(--body); width: 96px; }
  .event-join {
    width: 165px; height: 25px; border-radius: 4px; display: flex; overflow: hidden;
    background: var(--tan);
  }
  .event-join span { flex: 1; font-size: 8.5px; color: #5e5548; line-height: 25px; padding-left: 6px; white-space: nowrap; }
  .event-join b {
    width: 31px; background: var(--tan-dark); color: var(--white);
    font-family: "Francois One", sans-serif; font-weight: 400; font-size: 14px;
    text-align: center; line-height: 25px;
  }
  .event-divider { left: 652px; top: 512px; width: 6px; height: 120px;
    background: linear-gradient(90deg, rgba(0,0,0,.06), rgba(255,255,255,.6)); }

  /* Info panel */
  .info-panel {
    left: 154px; top: 667px; width: 692px; height: 343px; background: var(--panel);
    box-shadow: 0 2px 7px rgba(0,0,0,.18);
  }
  .about-box { left: 181px; top: 693px; width: 367px; height: 292px; background: var(--panel-inner); }
  .about-copy {
    left: 191px; top: 708px; width: 345px; font-size: 10px; line-height: 13px; color: var(--body);
  }
  .about-copy p + p { margin-top: 13px; }
  .meet-label { font-size: 10px; font-weight: 700; color: var(--ink); text-transform: uppercase; }
  .meet-value { font-size: 10px; line-height: 13px; color: var(--body); }
  .map-frame { left: 572px; top: 832px; width: 250px; height: 153px; background: var(--white); }
  .map-area {
    left: 578px; top: 838px; width: 238px; height: 141px;
    background: linear-gradient(180deg, #e8e4dc, #e0dbd1);
  }

  /* Footer */
  .like-pill {
    left: 155px; top: 1034px; height: 15px; width: 33px; border: 1px solid #9aa6c0;
    background: #eef1f7; font-size: 8px; color: #3b4f80; line-height: 13px; text-align: center; border-radius: 2px;
  }
  .like-text { left: 194px; top: 1036px; font-size: 8.5px; color: var(--body); }
  .follow-pill {
    left: 408px; top: 1035px; height: 14px; width: 42px; border: 1px solid #9fc3dc;
    background: #e6f2fa; font-size: 8px; color: #2a5f88; line-height: 12px; text-align: center; border-radius: 2px;
  }
  .social-link {
    top: 1032px; font-family: "Oswald", sans-serif; font-size: 12px; display: flex; gap: 6px;
    align-items: center; text-decoration: none;
  }
  .social-link i { width: 14px; height: 14px; border-radius: 50%; display: block; }
  .partners { left: 155px; top: 1064px; }
  .partner {
    position: absolute; top: 0; width: 64px; height: 66px; background: var(--white);
    box-shadow: 0 1px 4px rgba(0,0,0,.22); display: flex; align-items: center; justify-content: center;
  }
  .partner i { display: block; width: 40px; height: 40px; border-radius: 50%; background: #d4cfc8; }
  .partner i.sq { border-radius: 4px; height: 24px; width: 46px; }
  .copyright { left: 154px; top: 1182px; font-size: 8.5px; color: var(--muted); }
  .footer-nav { left: 695px; top: 1182px; font-size: 8.5px; color: var(--muted); word-spacing: 2px; }
</style>
</head>
<body>

<header>
  <div class="abs brand">
    <span class="brand-dot"></span>
    <span class="brand-name">Glad Tonight Walk</span>
  </div>
  <div class="abs party-art" role="img" aria-label="Cartoon illustration of two party-goers dancing with drinks"></div>
  <div class="abs party-art side" role="img" aria-label="Cartoon illustration of a party-goer holding a cocktail"></div>
  <a class="abs auth-btn login" href="#">LOGIN
    <svg width="8" height="10" viewBox="0 0 8 10"><path d="M1 1l5 4-5 4" stroke="#fff" stroke-width="2" fill="none"/></svg></a>
  <a class="abs auth-btn signup" href="#">SIGNUP
    <svg width="8" height="10" viewBox="0 0 8 10"><path d="M1 1l5 4-5 4" stroke="#fff" stroke-width="2" fill="none"/></svg></a>
  <div class="abs banner">London's Biggest and Best Glad Tonight Walk</div>
</header>

<main>
  <h2 class="abs section-title" style="left:155px;top:208px;">Photo Gallery</h2>
  <div class="abs gallery-frame"></div>
  <div class="abs gallery-photo" role="img" aria-label="Photo of friends toasting with cocktails in a bar"></div>
  <div class="abs thumbs">
    <svg class="abs" style="left:0;top:9px" width="6" height="9" viewBox="0 0 6 9"><path d="M6 0L0 4.5 6 9z" fill="#d3281c"/></svg>
    <span class="thumb" role="img" aria-label="Gallery thumbnail" style="left:13px;background:#8a2c54"></span>
    <span class="thumb" role="img" aria-label="Gallery thumbnail" style="left:47px;background:#4c7d9a"></span>
    <span class="thumb" role="img" aria-label="Gallery thumbnail" style="left:81px;background:#6a5a7a"></span>
    <span class="thumb" role="img" aria-label="Gallery thumbnail" style="left:115px;background:#9a3a4a"></span>
    <span class="thumb" role="img" aria-label="Gallery thumbnail" style="left:149px;background:#4a3a3a"></span>
    <span class="thumb" role="img" aria-label="Gallery thumbnail" style="left:183px;background:#5c6e88"></span>
    <span class="thumb" role="img" aria-label="Gallery thumbnail" style="left:217px;background:#a04a6a"></span>
    <span class="thumb" role="img" aria-label="Gallery thumbnail" style="left:251px;background:#7a6a5a"></span>
    <svg class="abs" style="left:287px;top:9px" width="6" height="9" viewBox="0 0 6 9"><path d="M0 0l6 4.5L0 9z" fill="#d3281c"/></svg>
  </div>

  <h2 class="abs benefits-title">Come on a <em>Glad Tonight Walk</em> and get:</h2>
  <div class="abs dashed" style="left:505px;top:245px;width:341px;"></div>
  <div class="abs benefit" style="top:262px">
    <svg width="17" height="10" viewBox="0 0 17 10"><path d="M1 1v3q0 3 4 3h9M11 4l3 3-3 3" stroke="#3d8a1e" stroke-width="1.6" fill="none"/></svg>
    <span><strong>FREE</strong> entry to 5 of the coolest bars and clubs in London's West End</span>
  </div>
  <div class="abs benefit" style="top:317px">
    <svg width="17" height="10" viewBox="0 0 17 10"><path d="M1 1v3q0 3 4 3h9M11 4l3 3-3 3" stroke="#3d8a1e" stroke-width="1.6" fill="none"/></svg>
    <span><strong>A FREE</strong> shot at each venue</span>
  </div>
  <div class="abs benefit" style="top:352px">
    <svg width="17" height="10" viewBox="0 0 17 10"><path d="M1 1v3q0 3 4 3h9M11 4l3 3-3 3" stroke="#3d8a1e" stroke-width="1.6" fill="none"/></svg>
    <span><strong>TO JUMP</strong> the queue</span>
  </div>
  <div class="abs benefit" style="top:388px">
    <svg width="17" height="10" viewBox="0 0 17 10"><path d="M1 1v3q0 3 4 3h9M11 4l3 3-3 3" stroke="#3d8a1e" stroke-width="1.6" fill="none"/></svg>
    <span><strong>TO MEET</strong> friendly and fun people in an awesome atmosphere</span>
  </div>

  <section>
    <div class="abs signup-card"></div>
    <p class="abs signup-copy">We have free nights running all the time<br>(see calendar above) so enter your<br>e-mail address to receive details<br>on upcoming crawls</p>
    <div class="abs signup-band"></div>
    <div class="abs email-field"><span>Enter your email address</span><b>SUBMIT</b></div>
  </section>

  <h2 class="abs section-title" style="left:474px;top:477px;">Current Events</h2>
  <div class="abs event-divider"></div>

  <svg class="abs event-date" style="left:474px;top:514px" viewBox="0 0 34 52">
    <path d="M1 1h32v14q0 16-14 18v14h9v4H6v-4h9V33Q1 31 1 15z" fill="#13968f"/>
    <rect x="4" y="3" width="26" height="7" fill="#fff"/>
    <text x="17" y="9" font-size="7" font-family="Arimo, sans-serif" text-anchor="middle" fill="#0d7c76">NOV</text>
    <text x="17" y="24" font-size="13" font-family="Arimo, sans-serif" text-anchor="middle" fill="#fff">05</text>
  </svg>
  <h3 class="abs event-title" style="left:514px;top:513px">Event Title Goes Here...</h3>
  <p class="abs event-text" style="left:515px;top:530px">Lorem Ipsum is simply dummy text of the printing &amp; typesetting.</p>
  <div class="abs event-join" style="left:474px;top:602px"><span>Email email id to join this event</span><b>GO</b></div>

  <svg class="abs event-date" style="left:681px;top:514px" viewBox="0 0 34 52">
    <path d="M1 1h32v14q0 16-14 18v14h9v4H6v-4h9V33Q1 31 1 15z" fill="#13968f"/>
    <rect x="4" y="3" width="26" height="7" fill="#fff"/>
    <text x="17" y="9" font-size="7" font-family="Arimo, sans-serif" text-anchor="middle" fill="#0d7c76">NOV</text>
    <text x="17" y="24" font-size="13" font-family="Arimo, sans-serif" text-anchor="middle" fill="#fff">06</text>
  </svg>
  <h3 class="abs event-title" style="left:721px;top:513px">Event Title Goes Here...</h3>
  <p class="abs event-text" style="left:722px;top:530px">Lorem Ipsum is simply dummy text of the printing &amp; typesetting.</p>
  <div class="abs event-join" style="left:681px;top:602px"><span>Email email id to join this event</span><b>GO</b></div>

  <section>
    <div class="abs info-panel"></div>
    <div class="abs about-box"></div>
    <div class="abs about-copy">
      <p>We believe this crawl is an amazing way to experience London's<br>awesome nightlife and we don't charge you a penny. We love to party and we don't think a price should be put on that.</p>
      <p>We take you to the best bars and clubs with free shots, cheap drinks deals and queue jump included.</p>
      <p>Highlights include Menagerie bar, which is open until 3am, with the liveliest, biggest and best party in town, with a range of cocktails, premium beers and spirits for a fantastic night out).</p>
      <p>Cherry Lanterns bar presents the best in London's club scene as DJs play the ultimate in club grooves for your dancing pleasure.</p>
      <p>The Marlow Assembly bar is a place where new experiences can be gained. The unexpected, the beautiful and the bizarre are at every turn. A labyrinth of rooms<br>with six different bar experiences each totally unique.</p>
      <p>Entrance is normally £10 to these venues but you get in for free and you receive a free shot at each bar for coming with Glad Tonight Walk</p>
    </div>

    <h2 class="abs section-title" style="left:568px;top:686px;">Where to Meet</h2>
    <div class="abs meet-label" style="left:571px;top:716px">Start Time:</div>
    <div class="abs meet-value" style="left:571px;top:729px">19:30 and 20:30, every Monday to Saturday.</div>
    <div class="abs meet-label" style="left:571px;top:758px">Address:</div>
    <div class="abs meet-value" style="left:571px;top:771px">Tappers Camden,<br>12-14 Larkfield Row, NW9 9ZZ</div>
    <div class="abs meet-label" style="left:571px;top:813px">Directions:</div>
    <div class="abs map-frame"></div>
    <div class="abs map-area" role="img" aria-label="Street map showing the meeting point"></div>
  </section>
</main>

<footer>
  <div class="abs like-pill">Like</div>
  <div class="abs like-text">1851 likes. Sign Up to see what your friends like</div>
  <div class="abs follow-pill">Follow</div>
  <a class="abs social-link" style="left:602px;color:var(--social-dark)" href="#"><i style="background:var(--social-dark)"></i>Follow us on Chatterly</a>
  <a class="abs social-link" style="left:737px;color:var(--social-light)" href="#"><i style="background:var(--social-light)"></i>Follow us on Pinbird</a>

  <div class="abs partners">
    <div class="partner" style="left:0"><i></i></div>
    <div class="partner" style="left:79px"><i class="sq"></i></div>
    <div class="partner" style="left:157px"><i></i></div>
    <div class="partner" style="left:236px"><i class="sq"></i></div>
    <div class="partner" style="left:314px"><i></i></div>
    <div class="partner" style="left:393px"><i class="sq"></i></div>
    <div class="partner" style="left:471px"><i class="sq"></i></div>
    <div class="partner" style="left:550px"><i></i></div>
    <div class="partner" style="left:628px"><i class="sq"></i></div>
  </div>

  <div class="abs dashed" style="left:154px;top:1167px;width:692px;"></div>
  <div class="abs copyright">Copyright © 2011 GLAD TONIGHT WALK. All Rights Reserved.</div>
  <nav class="abs footer-nav">HOME | LOGIN | REGISTER | FAQ's</nav>
</footer>

</body>
</html>
```